Ridgeline Yard Works Stationary Package
Business Cards, Letterhead, Envelope, Sticker, Fax Cover sheet, invoice, and estimate
Ridgeline Yard Works Stationary Package - Construction
Creative Brief
Use same font as used in my logo
Pete Marrow
Owner
4172 W. Fenwick Rd. Burbank, IL 60421
petemarrow@quailnet.example
www.ridgelineyardworks.example
Can information be in a format that can be edited for future use. ex: Name Changes, New Numbers, etc?

```html
<!DOCTYPE html>
<html lang="en">
<head>
<meta charset="utf-8">
<title>Ridgeline Yard Works – Business Card</title>
<link rel="stylesheet" href="https://fonts.googleapis.com/css2?family=Exo+2:wght@400;500;600;700&family=Open+Sans:wght@400;600;700&display=swap">
<style>
  :root {
    --page-bg: #e9e9e7;
    --card-bg: #ffffff;
    --ink: #1d1d1f;
    --ink-soft: #333336;
    --rule: #c9c9c9;
    --brand-blue: #1f3f9a;
    --band-deep: #172a80;
    --band-light: #1f7bc6;
    --accent-red: #d6262b;
    --white: #ffffff;
  }
  * { margin: 0; padding: 0; box-sizing: border-box; }
  html, body {
    width: 1200px; height: 778px; overflow: hidden;
    background: var(--page-bg);
  }
  .business-card {
    position: absolute; left: 30px; top: 35px;
    width: 1140px; height: 708px;
    background: var(--card-bg);
    overflow: hidden;
    font-family: "Open Sans", Arial, sans-serif;
    color: var(--ink);
  }
  .brand-mark {
    position: absolute; left: 160px; top: 62px;
    width: 140px; height: 140px;
    background: var(--brand-blue);
    border-radius: 22px;
  }
  .brand-name {
    position: absolute; left: 326px; top: 78px;
    font-family: "Exo 2", Arial, sans-serif;
    font-weight: 600; font-size: 66px; line-height: 1;
    color: var(--ink); white-space: nowrap;
  }
  .brand-tagline {
    position: absolute; left: 334px; top: 154px; width: 730px;
    display: flex; align-items: center; gap: 18px;
    font-family: "Exo 2", Arial, sans-serif;
    font-size: 27px; color: var(--ink); white-space: nowrap;
  }
  .brand-tagline::before, .brand-tagline::after {
    content: ""; flex: 1; height: 3px; background: var(--ink);
  }
  .contact-divider {
    position: absolute; left: 567px; top: 252px;
    width: 2px; height: 222px; background: var(--rule);
  }
  .person {
    position: absolute; right: 661px; top: 330px; text-align: right;
  }
  .person-name { font-weight: 700; font-size: 42px; line-height: 1.1; }
  .person-role { font-weight: 600; font-size: 29px; line-height: 1.4; }
  .contact-details {
    position: absolute; left: 646px; top: 268px;
    font-size: 26px; line-height: 47px; color: var(--ink-soft);
  }
  .address { margin-bottom: 20px; }
  .contact-line { display: flex; align-items: center; gap: 12px; }
  .contact-line svg { width: 24px; height: 24px; flex: none; }
  .card-band { position: absolute; left: 0; bottom: 0; width: 1140px; height: 200px; }
  .website {
    position: absolute; left: 0; width: 1140px; top: 570px;
    text-align: center; color: var(--white);
    font-weight: 700; font-size: 28px; letter-spacing: 2px;
  }
</style>
</head>
<body>
  <div class="business-card">
    <div class="brand-mark"></div>
    <div class="brand-name">Ridgeline Yard Works</div>
    <div class="brand-tagline">Home Restoration Specialists</div>

    <div class="contact-divider"></div>

    <div class="person">
      <div class="person-name">Pete Marrow</div>
      <div class="person-role">Owner</div>
    </div>

    <div class="contact-details">
      <div class="address">4172 W. Fenwick Rd.<br>Burbank, IL 60421</div>
      <div class="contact-line">
        <svg viewBox="0 0 24 24" aria-hidden="true"><rect x="6" y="1" width="12" height="22" rx="2" fill="var(--accent-red)"/><rect x="8" y="4" width="8" height="12" fill="#fff"/></svg>
        (708) 555-0142
      </div>
      <div class="contact-line">
        <svg viewBox="0 0 24 24" aria-hidden="true"><path d="M3 9c0-3 4-5 9-5s9 2 9 5l-3 2-2-2V7H8v2l-2 2z" fill="var(--accent-red)"/><rect x="4" y="12" width="16" height="10" rx="2" fill="var(--accent-red)"/></svg>
        (708) 555-0187
      </div>
      <div class="contact-line">
        <svg viewBox="0 0 24 24" aria-hidden="true"><rect x="2" y="5" width="20" height="14" fill="none" stroke="var(--accent-red)" stroke-width="2.4"/><path d="M2 6l10 7 10-7" fill="none" stroke="var(--accent-red)" stroke-width="2.4"/></svg>
        petemarrow@quailnet.example
      </div>
    </div>

    <svg class="card-band" viewBox="0 0 1140 200" preserveAspectRatio="none" aria-hidden="true">
      <defs>
        <linearGradient id="bandFill" x1="0" x2="1" y1="0" y2="0">
          <stop offset="0" stop-color="var(--band-deep)"/>
          <stop offset="0.5" stop-color="var(--band-light)"/>
          <stop offset="1" stop-color="var(--band-deep)"/>
        </linearGradient>
      </defs>
      <path d="M0 46 Q570 -8 1140 46 L1140 200 L0 200 Z" fill="var(--accent-red)"/>
      <path d="M0 58 Q570 6 1140 58 L1140 200 L0 200 Z" fill="url(#bandFill)"/>
    </svg>
    <div class="website">www.ridgelineyardworks.example</div>
  </div>
</body>
</html>
```